Conference banner for Kestrel Training organisation

We empower everyday heroes.
We provide training that empowers individuals to create positive change in themselves, their community, and the world.
We need a large banner design to promote the organisation at conferences and events. We are open to ideas and creativity.
It may involve creatively displaying our logo only, or it may involve our logo and a summary of our products (Kestrel training, Calm Minds Field Care).
Size: 820mm width x 1790mm height
300dpi
Target Market(s)
Educators and frontline health, community, and social workers.
Industry/Entity Type
Training
Colors
Designer to choose colors to be used in the design.

```html
<!DOCTYPE html>
<html lang="en">
<head>
<meta charset="utf-8">
<title>Kestrel Training Banner</title>
<link href="https://fonts.googleapis.com/css2?family=Oswald:wght@500;600;700&family=Roboto:ital,wght@0,400;1,700;1,900&display=swap" rel="stylesheet">
<style>
  :root {
    --maroon: #9b1f34;
    --maroon-deep: #7d1628;
    --rose: #c9566a;
    --white: #ffffff;
    --mist: #eceef1;
    --navy: #1f3f8f;
    --ink: #2b2b2b;
    --photo-skin: #e7c6aa;
    --photo-blue: #3b5f9a;
  }
  * { margin: 0; padding: 0; box-sizing: border-box; }
  html, body { width: 769px; height: 1200px; overflow: hidden; background: var(--white); }
  .banner { position: relative; width: 769px; height: 1200px; overflow: hidden; background: var(--white); font-family: "Roboto", sans-serif; }
  .banner-shapes { position: absolute; inset: 0; }
  .brand { position: absolute; top: 70px; left: 0; right: 0; display: flex; justify-content: center; align-items: center; gap: 14px; }
  .brand-dot { width: 34px; height: 34px; border-radius: 50%; background: var(--maroon); }
  .brand-name { font-family: "Oswald", sans-serif; font-weight: 600; font-size: 40px; letter-spacing: 1px; color: var(--navy); }
  .headline { position: absolute; left: 108px; top: 690px; color: var(--white); font-family: "Oswald", sans-serif; text-transform: uppercase; line-height: 1.05; }
  .headline-main { font-size: 66px; font-weight: 700; }
  .headline-sub { font-size: 44px; font-weight: 600; margin-top: 6px; line-height: 1.1; }
  .site-url { position: absolute; left: 110px; top: 930px; font-size: 22px; color: var(--white); letter-spacing: 0.5px; }
  .url-rule { position: absolute; left: 108px; top: 968px; width: 560px; height: 2px; background: rgba(255,255,255,0.35); }
  .certify { position: absolute; left: 190px; top: 1072px; display: flex; align-items: center; gap: 20px; }
  .certify-icon { width: 62px; height: 80px; }
  .certify-text { font-style: italic; font-weight: 700; color: var(--ink); line-height: 1.1; }
  .certify-lead { font-size: 28px; }
  .certify-main { font-size: 34px; font-weight: 900; color: var(--maroon-deep); }
</style>
</head>
<body>
<main class="banner">
  <svg class="banner-shapes" width="769" height="1200" viewBox="0 0 769 1200">
    <defs>
      <linearGradient id="photoFill" x1="0" y1="0" x2="1" y2="1">
        <stop offset="0" stop-color="#d9d3cf"/>
        <stop offset="0.45" stop-color="var(--photo-skin)"/>
        <stop offset="1" stop-color="var(--photo-blue)"/>
      </linearGradient>
    </defs>
    <path class="top-swoosh" d="M0 150 Q380 250 769 180 L769 290 L0 290 Z" fill="var(--mist)"/>
    <rect class="training-photo" role="img" aria-label="Photo of hands performing CPR on a training manikin" x="0" y="215" width="769" height="470" fill="url(#photoFill)"/>
    <path class="top-curve" d="M0 170 Q300 300 769 215 L769 150 L0 150 Z" fill="var(--white)"/>
    <path class="rose-wedge" d="M0 560 Q420 520 769 470 L769 640 L0 640 Z" fill="var(--rose)"/>
    <path class="maroon-band" d="M0 600 Q420 585 769 500 L769 1200 L0 1200 Z" fill="var(--maroon)"/>
    <path class="bottom-curve" d="M0 1000 Q400 1060 769 990 L769 1200 L0 1200 Z" fill="var(--white)"/>
    <path class="bottom-edge" d="M0 1010 Q400 1075 769 1000" fill="none" stroke="var(--mist)" stroke-width="10"/>
  </svg>

  <div class="brand">
    <span class="brand-dot"></span>
    <span class="brand-name">KESTREL WORKS</span>
  </div>

  <div class="headline">
    <div class="headline-main">Kestrel Training</div>
    <div class="headline-sub">Calm Minds<br>Field Care</div>
  </div>

  <div class="site-url">www.kestrelworks.org</div>
  <div class="url-rule"></div>

  <div class="certify">
    <svg class="certify-icon" viewBox="0 0 62 80">
      <path d="M18 44 L8 76 L20 68 L26 78 L31 52 Z" fill="#555"/>
      <path d="M44 44 L54 76 L42 68 L36 78 L31 52 Z" fill="#555"/>
      <circle cx="31" cy="30" r="27" fill="#444"/>
      <circle cx="31" cy="30" r="19" fill="none" stroke="#fff" stroke-width="2.5"/>
      <path d="M22 30 L29 37 L41 24" fill="none" stroke="#fff" stroke-width="4" stroke-linecap="round" stroke-linejoin="round"/>
    </svg>
    <div class="certify-text">
      <div class="certify-lead">Get Certified</div>
      <div class="certify-main">FIRST AID TRAINING!</div>
    </div>
  </div>
</main>
</body>
</html>
```